Independence Day Graphics for Sale

I want to create 10 social media graphics (new Pictora size 4:5 (1080 x 1350 pixels) focusing on our July 4th Sale Graphics, using any of the pics attached. Use the attached pics, NO RANDOM STOCK PHOTOGRAPHY. For the color scheme of the graphics, they should all be complementary to the product colors in the photos.
You can add any of the photos attached but none are required. You can do some of the graphics in all text. I mainly need BOLD text that says one of the headlines (10 total) SEE ATTACHED WORD DOCUMENT for the headlines to use.

Target Market(s)

women looking to lose weight

Requirements
Must have
• pics attached and text attached

```html
<!DOCTYPE html>
<html lang="en">
<head>
<meta charset="UTF-8">
<title>Historic 4th of July Sale</title>
<link href="https://fonts.googleapis.com/css2?family=Anton&family=Montserrat:wght@700;800;900&display=swap" rel="stylesheet">
<style>
  :root {
    --backdrop: #283150;
    --navy-deep: #040826;
    --navy: #0a1450;
    --navy-bright: #03136a;
    --white: #ffffff;
    --red: #e3101c;
    --firework-red: #ff4a4a;
    --firework-blue: #2e86ff;
  }
  * { margin: 0; padding: 0; box-sizing: border-box; }
  html, body {
    width: 1200px;
    height: 1000px;
    overflow: hidden;
    background: var(--backdrop);
  }
  .poster {
    position: absolute;
    left: 285px;
    top: 106px;
    width: 630px;
    height: 788px;
    overflow: hidden;
    background: linear-gradient(180deg, var(--navy-deep) 0%, var(--navy) 45%, var(--navy-bright) 100%);
  }
  .firework {
    position: absolute;
    border-radius: 50%;
  }
  .firework--red {
    left: -120px;
    top: -150px;
    width: 420px;
    height: 460px;
    background: radial-gradient(circle at 45% 40%, rgba(255,120,120,0.95) 0%, rgba(240,60,70,0.75) 25%, rgba(180,20,50,0.35) 50%, rgba(60,10,40,0) 70%);
  }
  .firework--blue {
    left: 400px;
    top: -80px;
    width: 340px;
    height: 380px;
    background: radial-gradient(circle at 50% 45%, rgba(150,210,255,0.95) 0%, rgba(46,134,255,0.75) 25%, rgba(20,70,200,0.35) 50%, rgba(10,20,90,0) 70%);
  }
  .headline {
    position: absolute;
    left: 0;
    width: 100%;
    text-align: center;
    color: var(--white);
    font-family: 'Anton', sans-serif;
    line-height: 1;
  }
  .headline--historic {
    top: 20px;
    font-size: 124px;
    letter-spacing: -1px;
    transform: scaleX(0.86);
  }
  .headline--sale {
    top: 197px;
    font-size: 124px;
    letter-spacing: -1px;
    transform: scaleX(0.9);
  }
  .occasion {
    position: absolute;
    left: 0;
    top: 152px;
    width: 100%;
    text-align: center;
    font-family: 'Montserrat', sans-serif;
    font-weight: 900;
    font-size: 46px;
    line-height: 1;
    color: var(--red);
    letter-spacing: -1px;
    -webkit-text-stroke: 3px var(--white);
    paint-order: stroke fill;
  }
  .occasion sup {
    font-size: 24px;
    vertical-align: 18px;
    margin-left: -2px;
    margin-right: 6px;
  }
  .product-lineup {
    position: absolute;
    left: 46px;
    top: 340px;
    width: 531px;
    height: 317px;
    border-radius: 18px;
    background: linear-gradient(180deg, rgba(245,245,248,0.92) 0%, rgba(225,225,232,0.9) 60%, rgba(200,120,170,0.55) 100%);
  }
  .offer {
    position: absolute;
    left: 44px;
    top: 658px;
    font-family: 'Montserrat', sans-serif;
    color: var(--white);
    line-height: 1;
  }
  .offer__percent {
    font-size: 62px;
    font-weight: 900;
    letter-spacing: -3px;
    color: var(--red);
    -webkit-text-stroke: 3px var(--white);
    paint-order: stroke fill;
  }
  .offer__off {
    font-size: 33px;
    font-weight: 800;
    margin-left: 6px;
  }
  .offer__scope {
    display: block;
    margin-top: 6px;
    margin-left: 4px;
    font-size: 34px;
    font-weight: 800;
  }
</style>
</head>
<body>
  <main class="poster">
    <div class="firework firework--red" role="img" aria-label="Red firework burst"></div>
    <div class="firework firework--blue" role="img" aria-label="Blue firework burst"></div>

    <h1 class="headline headline--historic">HISTORIC</h1>
    <p class="occasion">4<sup>TH</sup>OF JULY</p>
    <p class="headline headline--sale">SALE!</p>

    <div class="product-lineup" role="img" aria-label="Four white supplement bottles standing in a row"></div>

    <p class="offer">
      <span class="offer__percent">25%</span><span class="offer__off">OFF</span>
      <span class="offer__scope">EVERYTHING</span>
    </p>
  </main>
</body>
</html>
```